Criação de Papelaria (6 itens) para Decoração & Mobília
A empresa queria:
" É um comércio de móveis planejados e móveis complementares, como sofás, cadeiras, banquetas e mesas. "

```html
<!DOCTYPE html>
<html lang="pt-BR">
<head>
<meta charset="UTF-8">
<title>Casalto — Pasta de apresentação</title>
<link rel="stylesheet" href="https://fonts.googleapis.com/css2?family=Montserrat:wght@500;600&display=swap">
<style>
  :root {
    --backdrop: #e7e5e3;
    --paper-light: #f7f7f8;
    --paper-shade: #dcdcdf;
    --circle-light: #e9e2e3;
    --navy-deep: #0b0d1c;
    --navy-mid: #1a1d33;
    --circle-dark: #22263e;
    --ink: #1b1b22;
    --maroon: #8a2332;
    --white: #ffffff;
    --muted: #4a4a52;
  }
  html, body {
    margin: 0;
    width: 1200px;
    height: 1200px;
    overflow: hidden;
    background: var(--backdrop);
    font-family: "Montserrat", sans-serif;
  }
  .folder-spread {
    position: absolute;
    left: 100px;
    top: 246px;
    width: 1000px;
    height: 708px;
    display: flex;
    box-shadow: 0 18px 40px rgba(0,0,0,0.18);
  }
  .panel {
    position: relative;
    width: 500px;
    height: 708px;
    overflow: hidden;
  }
  .panel-inside {
    background: linear-gradient(100deg, var(--paper-shade) 0%, var(--paper-light) 45%, #ececee 100%);
  }
  .panel-inside .top-rule {
    position: absolute;
    top: 0; left: 0; right: 0;
    height: 5px;
    background: var(--maroon);
  }
  .panel-inside .halo {
    position: absolute;
    width: 440px;
    height: 440px;
    border-radius: 50%;
    left: 230px;
    top: 20px;
    background: var(--circle-light);
  }
  .panel-cover {
    background: linear-gradient(160deg, var(--navy-mid) 0%, var(--navy-deep) 70%);
  }
  .panel-cover .halo {
    position: absolute;
    width: 440px;
    height: 440px;
    border-radius: 50%;
    left: -220px;
    top: 20px;
    background: var(--circle-dark);
    opacity: 0.7;
  }
  .wordmark {
    position: absolute;
    margin: 0;
    font-weight: 600;
    font-size: 46px;
    letter-spacing: 6px;
    text-transform: uppercase;
    line-height: 1;
  }
  .panel-inside .wordmark {
    left: 80px;
    top: 344px;
    color: var(--ink);
  }
  .panel-cover .wordmark {
    left: 124px;
    top: 288px;
    color: var(--white);
  }
  .contacts {
    position: absolute;
    left: 110px;
    bottom: 44px;
    display: grid;
    grid-template-columns: auto auto;
    column-gap: 26px;
    row-gap: 6px;
    font-size: 10px;
    font-weight: 500;
    color: var(--muted);
  }
  .contact-item {
    display: flex;
    align-items: center;
    gap: 6px;
  }
  .contact-item svg {
    width: 11px;
    height: 11px;
    fill: none;
    stroke: var(--muted);
    stroke-width: 1.6;
  }
</style>
</head>
<body>
  <main class="folder-spread">
    <section class="panel panel-inside">
      <div class="top-rule"></div>
      <div class="halo"></div>
      <p class="wordmark">Casalto</p>
      <div class="contacts">
        <div class="contact-item">
          <svg viewBox="0 0 12 12"><path d="M3 1h2l1 3-1.5 1a6 6 0 0 0 2.5 2.5L8 6l3 1v2a1.5 1.5 0 0 1-1.5 1.5A8.5 8.5 0 0 1 1.5 2.5 1.5 1.5 0 0 1 3 1z"/></svg>
          <span>+55 00 0000-0000</span>
        </div>
        <div class="contact-item">
          <svg viewBox="0 0 12 12"><path d="M3 1h2l1 3-1.5 1a6 6 0 0 0 2.5 2.5L8 6l3 1v2a1.5 1.5 0 0 1-1.5 1.5A8.5 8.5 0 0 1 1.5 2.5 1.5 1.5 0 0 1 3 1z"/></svg>
          <span>+55 00 0000-0000</span>
        </div>
        <div class="contact-item">
          <svg viewBox="0 0 12 12"><rect x="1" y="2.5" width="10" height="7" rx="1"/><path d="M1 3l5 3.5L11 3"/></svg>
          <span>contato@casalto.com</span>
        </div>
        <div class="contact-item">
          <svg viewBox="0 0 12 12"><circle cx="6" cy="6" r="5"/><path d="M1 6h10M6 1c2 2 2 8 0 10M6 1c-2 2-2 8 0 10"/></svg>
          <span>www.casalto.com</span>
        </div>
        <div class="contact-item">
          <svg viewBox="0 0 12 12"><path d="M6 11S2 7 2 4.5a4 4 0 0 1 8 0C10 7 6 11 6 11z"/><circle cx="6" cy="4.5" r="1.3"/></svg>
          <span>Rua das Flores, 120</span>
        </div>
      </div>
    </section>
    <section class="panel panel-cover">
      <div class="halo"></div>
      <p class="wordmark">Casalto</p>
    </section>
  </main>
</body>
</html>
```